BrightPine Real Estate Sign

We are in the process of rebranding our business and need a new For Sale \ Sold sign.
We're a prestige real estate agency and therefore require a really stylish sign.
I've uploaded the following files
1. The new company logo
2. "sample sign.jpg" which shows the type of sign we would like. It is a metal sign with a top panel and bottom panel.
3. Our previous sign "previous sign.jpg" if you're interested in seeing it.
The sign must be black with white text.
Our thoughts are that the top panel (refer to sample sign) would contain the text "For Sale" or "Sold". These would be two separate panels which are interchangeable and could be screwed in place.
The bottom panel would not contain any photos like the sample. However, it may contain our logo and my contact details etc.
The sign is 900mm wide x 1200mm high.
My details are:
Name: Gareth Wimble
Web: www.bprealestate.com.au
Email: sales@bprealestate.com.au
Phone: 0491 650 387

```html
<!DOCTYPE html>
<html lang="en">
<head>
<meta charset="utf-8">
<title>BrightPine Real Estate – For Sale Sign</title>
<link rel="stylesheet" href="https://fonts.googleapis.com/css2?family=Archivo:wdth,wght@62..125,100..900&family=Arimo:wght@400;700&display=swap">
<style>
  :root {
    --sign-black: #1c1a1b;
    --panel-rule: #4a4647;
    --text-white: #ffffff;
  }
  * { margin: 0; padding: 0; box-sizing: border-box; }
  html, body {
    width: 900px;
    height: 1200px;
    overflow: hidden;
    background: var(--sign-black);
  }
  .sign {
    position: relative;
    width: 900px;
    height: 1200px;
    overflow: hidden;
    background: var(--sign-black);
    color: var(--text-white);
  }

  /* Brand panel */
  .brand-panel {
    position: absolute;
    left: 0; top: 0;
    width: 900px; height: 316px;
    background: var(--sign-black);
    border-bottom: 3px solid var(--panel-rule);
  }
  .brand-square {
    position: absolute;
    left: 50px; top: 106px;
    width: 128px; height: 128px;
    background: var(--text-white);
  }
  .brand-divider {
    position: absolute;
    left: 230px; top: 48px;
    width: 3px; height: 257px;
    background: var(--text-white);
  }
  .brand-name {
    position: absolute;
    left: 272px; top: 104px;
    width: 600px;
    font-family: "Archivo", sans-serif;
    text-align: center;
    line-height: 1;
  }
  .brand-name .brand-word {
    display: block;
    font-size: 96px;
    font-weight: 700;
    letter-spacing: -1px;
  }
  .brand-name .brand-descriptor {
    display: block;
    margin-top: 12px;
    font-size: 32px;
    font-weight: 400;
    letter-spacing: 0.24em;
    padding-left: 0.24em;
  }

  /* Headline panel */
  .headline-panel {
    position: absolute;
    left: 0; top: 316px;
    width: 900px; height: 430px;
    background: var(--sign-black);
    border-bottom: 3px solid var(--panel-rule);
  }
  .headline {
    position: absolute;
    left: 0;
    width: 900px;
    font-family: "Archivo", sans-serif;
    font-weight: 900;
    font-variation-settings: "wdth" 125;
    font-stretch: 125%;
    font-size: 212px;
    line-height: 1;
    text-align: center;
    transform: scaleX(1.25);
    transform-origin: center;
  }
  .headline-for {
    top: 7px;
    letter-spacing: 58px;
    padding-left: 58px;
  }
  .headline-sale {
    top: 234px;
    letter-spacing: 8px;
    padding-left: 8px;
  }

  /* Contact panel */
  .contact-panel {
    position: absolute;
    left: 0; top: 746px;
    width: 900px; height: 454px;
    background: var(--sign-black);
    font-family: "Arimo", sans-serif;
  }
  .agent-name,
  .agent-phone,
  .contact-web,
  .contact-email {
    position: absolute;
    line-height: 1;
    white-space: nowrap;
  }
  .agent-name {
    left: 76px; top: 54px;
    font-size: 100px;
    font-weight: 700;
  }
  .agent-phone {
    left: 76px; top: 156px;
    font-size: 100px;
    font-weight: 700;
    letter-spacing: 10px;
  }
  .contact-web {
    left: 30px; top: 296px;
    font-size: 66px;
    font-weight: 400;
  }
  .contact-email {
    left: 30px; top: 371px;
    font-size: 66px;
    font-weight: 400;
  }
</style>
</head>
<body>
  <main class="sign">
    <header class="brand-panel">
      <div class="brand-square"></div>
      <div class="brand-divider"></div>
      <div class="brand-name">
        <span class="brand-word">BrightPine</span>
        <span class="brand-descriptor">REAL ESTATE</span>
      </div>
    </header>

    <section class="headline-panel">
      <div class="headline headline-for">FOR</div>
      <div class="headline headline-sale">SALE</div>
    </section>

    <footer class="contact-panel">
      <div class="agent-name">Gareth Wimble</div>
      <div class="agent-phone">0491 650 387</div>
      <div class="contact-web">www.bprealestate.com.au</div>
      <div class="contact-email">sales@bprealestate.com.au</div>
    </footer>
  </main>
</body>
</html>
```